Design clean technology service-based company website

Hello, We are looking to reskin our company website. We are an environmental inspection company and test for Asbestos, Lead and Mold along with other contaminants. People depend on the results to be accurate and fast. We are regulated by the EPA and State regulations. We work a lot with business to business and business to customer. We are wanting to make our new presentation to be modern and easy for customers to interact with us, understand our process and services while providing valuable environmental informational resource and updates. We are a technology based company and will be providing instantaneous results as reports come in for the customers. We are needing good calls to action on the site to direct them to setup a new inspection. Each user will have a backend access to their job information with invoices, reports, status, etc. We have developed software to be able to proved these reports and want to look the part.

My current website is www.trypelmarix.com

Helllo we are wanting to make sure we have good time to select the right website for us and also have the additional time to select other pages of the website. We have received great designs and have consolidated our requests into a document for the next set of iterations.

Target Market(s)

Home Owners, Contractors, Engineers, Real Estate Agents, Building Owners, Insurance Adjusters

Industry/Entity Type

Environmental Consultant

Number of Pages Required

5+ page

Font styles to use
Sans Serif

Colors
0355a3
9bcb3c
7f7f7f
f5f5f5
000000

Requirements
Must have
• Use our existing logo to design around
• The layouts look good in mobile mode for understanding and selecting services and signing up
• Clean Modern Layout
• Have all pages on the website have a similar layout and feel
• Clearly communicate services along with bundle service packages
• Detail the customer journey with graphic design
• Great call to actions to either schedule inspection online, call, text, chat
Nice to have
• Have an interactive graphic for where to test for lead, asbestos and mold.
• I like the barney kolts top order line bar - see attached
• Have clear question and answer page layouts for asbestos, lead and mold
• Show Company reviews
• Have clear Resources pages for all types of contaminants
Should not have
• My current website is www.trypelmarix.com

```html
<!DOCTYPE html>
<html lang="en">
<head>
<meta charset="utf-8">
<title>Pelmarix Environmental Inspections</title>
<link href="https://fonts.googleapis.com/css2?family=Open+Sans:wght@400;600;700&display=swap" rel="stylesheet">
<style>
:root{
  --green:#56b81f;
  --green-dark:#4aa318;
  --grey:#6d6d6d;
  --grey-light:#9a9a9a;
  --line:#dcdcdc;
  --band:#efefef;
  --footer:#2e2e2e;
  --ink:#333;
  --white:#fff;
}
*{box-sizing:border-box;margin:0;padding:0}
html,body{width:1200px;height:3579px;overflow:hidden}
body{position:relative;font-family:'Open Sans',Arial,sans-serif;color:var(--ink);background:var(--white)}
.abs{position:absolute}
.center{text-align:center;left:0;width:1200px}

/* hero */
.hero{left:0;top:0;width:1200px;height:709px;background:linear-gradient(120deg,#c9ccc8 0%,#a9aca8 40%,#d8dad6 70%,#b5b8b3 100%)}
.nav{left:0;top:0;width:1200px;height:70px;display:flex;justify-content:center;gap:48px;padding-top:22px}
.nav a{color:var(--green);font-size:17px;text-decoration:none;text-transform:uppercase;letter-spacing:.3px}
.nav a.active{color:var(--white);border-bottom:2px solid var(--white);padding-bottom:6px;height:30px}
.brand-name{top:298px;font-size:150px;font-weight:700;color:var(--green);letter-spacing:2px;line-height:1}
.brand-sub{top:428px;font-size:34px;color:#555;letter-spacing:9px;text-transform:uppercase}

/* services */
.dash{left:0;top:708px;width:1200px;border-top:3px dashed var(--green)}
.service-ring{width:152px;height:152px;border-radius:50%;border:6px solid var(--green);background:var(--white);top:633px;display:flex;align-items:center;justify-content:center}
.service-label{top:812px;width:300px;text-align:center;font-size:19px;font-weight:700;color:#333}

.section-title{font-size:43px;font-weight:700;color:#555}
.section-title span{color:var(--green)}
.intro{top:900px}
.intro-text{left:198px;top:972px;width:804px;font-size:15.5px;line-height:26px;color:#555;text-align:center}
.intro-text p+p{margin-top:2px}

/* video */
.video{left:0;top:1210px;width:1200px;height:417px;background:linear-gradient(100deg,#3b3b3b 0%,#5a5a55 45%,#4b4b45 75%,#2e2e2e 100%)}
.play{left:539px;top:1324px}
.video-title{top:1490px;font-size:43px;font-weight:700;color:var(--white)}
.video-link{top:1553px;font-size:18px;color:var(--white);text-decoration:underline}

/* owner */
.owner-frame{left:124px;top:1737px;width:260px;height:296px;border:14px solid #d5d5d5}
.owner-photo{left:95px;top:1701px;width:258px;height:303px;background:linear-gradient(160deg,#6aa44a,#4d7d37 50%,#7d8793)}
.owner-role{left:439px;top:1782px;font-size:40px;font-weight:700;color:var(--green)}
.owner-name{left:439px;top:1842px;font-size:21px;color:#444}
.owner-bio{left:439px;top:1884px;width:660px;font-size:15.5px;line-height:25px;color:#555}

/* coverage */
.coverage{left:0;top:2114px;width:1200px;height:310px;background:linear-gradient(100deg,#f4f4f4,#e4e5e3 60%,#ececeb)}
.coverage-title{top:2162px;font-size:35px;font-weight:700;color:var(--green)}
.coverage-sub{top:2220px;font-size:19px;color:#444}
.project-title{left:76px;top:2268px;font-size:33px;font-weight:700;color:var(--green)}
.project-text{left:76px;top:2323px;width:640px;font-size:14.5px;line-height:23px;color:#555}
.btn{background:var(--green);color:var(--white);font-weight:700;text-transform:uppercase;display:flex;align-items:center;justify-content:center;border-radius:3px}
.btn-contact{left:914px;top:2300px;width:207px;height:50px;font-size:20px}

/* contact */
.touch{top:2468px}
.info-box{top:2541px;width:324px;height:177px;border:1.5px solid var(--line);display:flex;flex-direction:column;align-items:center;padding-top:56px;font-size:15.5px;color:#555;text-align:center;line-height:23px}
.info-box svg{margin-bottom:14px}
.field{height:44px;border-bottom:1.5px solid var(--line);font-size:15.5px;color:#8a8a8a;padding:12px 0 0 20px}
.btn-send{left:523px;top:2966px;width:155px;height:45px;font-size:19px}

/* accreditation */
.badges{left:0;top:3088px;width:1200px;height:207px;background:var(--band)}
.badge{background:#9a9a9a}

/* footer */
.footer{left:0;top:3295px;width:1200px;height:284px;background:var(--footer)}
.footer-brand{top:3337px;font-size:44px;font-weight:700;color:var(--white)}
.footer-nav{left:0;width:1200px;top:3417px;display:flex;justify-content:center;gap:40px}
.footer-nav a{color:var(--white);font-size:16px;text-decoration:none}
.copyright{top:3461px;font-size:14.5px;color:#ddd}
.social{left:0;width:1200px;top:3496px;display:flex;justify-content:center;gap:12px}
.social span{width:42px;height:42px;border-radius:50%;border:2px solid #cfcfcf}
</style>
</head>
<body>

<div class="abs hero" role="img" aria-label="Inspectors in white protective suits and respirators working on a roof"></div>
<nav class="abs nav">
  <a class="active" href="#">Home</a><a href="#">Our Services</a><a href="#">Resources</a><a href="#">Blog</a><a href="#">Q &amp; A</a><a href="#">Reviews</a><a href="#">Connect</a>
</nav>
<div class="abs center brand-name">Pelmarix</div>
<div class="abs center brand-sub">Environmental Inspections</div>

<div class="abs dash"></div>
<div class="abs service-ring" style="left:158px">
  <svg width="62" height="62" viewBox="0 0 62 62"><circle cx="31" cy="26" r="15" fill="none" stroke="#333" stroke-width="4"/><circle cx="25" cy="24" r="4" fill="#333"/><circle cx="37" cy="24" r="4" fill="#333"/><circle cx="16" cy="42" r="7" fill="#333"/><circle cx="46" cy="42" r="7" fill="#333"/><rect x="26" y="40" width="10" height="10" fill="#333"/></svg>
</div>
<div class="abs service-ring" style="left:523px">
  <svg width="62" height="62" viewBox="0 0 62 62"><path d="M10 30 L31 12 L52 30" fill="none" stroke="#333" stroke-width="4"/><path d="M16 26 V50 H46 V26" fill="none" stroke="#333" stroke-width="4"/><circle cx="27" cy="38" r="3" fill="#333"/><circle cx="35" cy="33" r="2" fill="#333"/><circle cx="36" cy="42" r="2.5" fill="#333"/></svg>
</div>
<div class="abs service-ring" style="left:890px">
  <svg width="62" height="62" viewBox="0 0 62 62"><rect x="30" y="10" width="18" height="14" transform="rotate(45 39 17)" fill="#333"/><path d="M30 30 L14 46 L18 50 L34 34" fill="none" stroke="#333" stroke-width="5"/></svg>
</div>
<div class="abs service-label" style="left:84px">Asbestos Testing</div>
<div class="abs service-label" style="left:449px">Mold Testing</div>
<div class="abs service-label" style="left:816px">Lead Based Paint Testing</div>

<h1 class="abs center section-title intro"><span>Environmental</span> Testing Evolved</h1>
<div class="abs intro-text">
  <p>Pelmarix grew up in the rough and tumble disaster restoration industry. Time and time again, we saw projects small and large brought to a stand-still to await environmental testing and results.</p>
  <p>First, we had to know when it's prudent or even required by law to test for asbestos, lead-based paint, mold or other contaminants. Then we had to track down reliable testing companies, facilities or equipment. Next, we had to ensure we safeguarded people and property in the process of obtaining test samples. Finally, we had to wait, sometimes days or even weeks, while property owners languished and spent more and more money on expensive temporary living or working space. We just knew there had to be a better way.</p>
</div>

<div class="abs video" role="img" aria-label="Technician in protective suit spraying a sealed plastic containment area"></div>
<svg class="abs play" width="122" height="122" viewBox="0 0 122 122"><circle cx="61" cy="61" r="55" fill="none" stroke="#56b81f" stroke-width="8"/><path d="M48 36 L86 61 L48 86 Z" fill="#56b81f"/></svg>
<div class="abs center video-title">Click Here to Watch Our Videos</div>
<div class="abs center video-link">View more videos</div>

<div class="abs owner-frame"></div>
<div class="abs owner-photo" role="img" aria-label="Portrait photo of the company owner outdoors"></div>
<h2 class="abs owner-role">Owner</h2>
<div class="abs owner-name">Dana Whitlock</div>
<p class="abs owner-bio">In his experience with inspecting property and mitigating environmental issues, Dana saw one project after another brought to a standstill awaiting testing results. He believed property owners should be able to get test results in hours, not days. Pelmarix was born.</p>

<div class="abs coverage" role="img" aria-label="Faded photo of an inspector at work on a rooftop"></div>
<h2 class="abs center coverage-title">Proudly Serving Dener - Colorado Sorings - Builder</h2>
<div class="abs center coverage-sub">Commercial Services | Residencial Services | Homeowner &amp; Contractor Services</div>
<h3 class="abs project-title">New construction project?</h3>
<p class="abs project-text">Let us start you in the right direction with our certified asbestos inspections<br>...Residential, commercial, schools, governmental properties, multi-family and more.</p>
<a class="abs btn btn-contact">Contact Us</a>

<h2 class="abs center section-title touch" style="font-size:40px"><span>Get in</span> Touch</h2>
<div class="abs info-box" style="left:76px">
  <svg width="40" height="40" viewBox="0 0 40 40"><path d="M9 3 L15 3 L18 12 L13 16 Q17 24 24 27 L28 22 L37 25 L37 31 Q37 37 31 37 Q3 33 3 9 Q3 3 9 3 Z" fill="#555"/></svg>
  555-014-2290
</div>
<div class="abs info-box" style="left:439px">
  <svg width="30" height="42" viewBox="0 0 30 42"><path d="M15 1 C6 1 1 8 1 15 C1 25 15 41 15 41 C15 41 29 25 29 15 C29 8 24 1 15 1 Z" fill="#555"/><circle cx="15" cy="15" r="5" fill="#fff"/></svg>
  2240 Larkspur Ave. Ste. 310<br>Aspen Vale, Co. 80000
</div>
<div class="abs info-box" style="left:800px">
  <svg width="42" height="32" viewBox="0 0 42 32"><rect x="1" y="1" width="40" height="30" rx="3" fill="#555"/><path d="M2 3 L21 18 L40 3" fill="none" stroke="#fff" stroke-width="2.5"/></svg>
  info at trypelmarix.com
</div>

<div class="abs field" style="left:76px;top:2790px;width:322px">Your Name</div>
<div class="abs field" style="left:439px;top:2790px;width:322px">Your Email</div>
<div class="abs field" style="left:800px;top:2790px;width:324px">Your phone no.</div>
<div class="abs field" style="left:76px;top:2873px;width:1048px">Your Message</div>
<a class="abs btn btn-send">Send</a>

<div class="abs badges"></div>
<div class="abs badge" style="left:78px;top:3160px;width:120px;height:60px;border-radius:4px"></div>
<div class="abs badge" style="left:292px;top:3158px;width:72px;height:72px;border-radius:50%"></div>
<div class="abs badge" style="left:536px;top:3140px;width:104px;height:104px;border-radius:50%"></div>
<div class="abs badge" style="left:722px;top:3166px;width:188px;height:48px;border-radius:4px"></div>
<div class="abs badge" style="left:933px;top:3156px;width:190px;height:70px;border-radius:8px"></div>

<footer class="abs footer"></footer>
<div class="abs center footer-brand">Pelmarix</div>
<nav class="abs footer-nav"><a href="#">Home</a><a href="#">Our Services</a><a href="#">Resources</a><a href="#">Blog</a><a href="#">Q &amp; A</a><a href="#">Reviews</a><a href="#">Connect</a></nav>
<div class="abs center copyright">©Pelmarix - 2017. All Rights Reserved.</div>
<div class="abs social"><span></span><span></span><span></span><span></span><span></span></div>

</body>
</html>
```